Fast Growing Personal Injury Law Firm Needs Business Card Design

We need a business card design for a fast growing personal injury law firm in Florida. Our name is Dorian Halvorsk, P.A. Our practice is comprised of younger attorneys (in their 30s) that employ more modern techniques/tools than our older competition. We would prefer a look that is a modern play on a classic look. Also, we would like to continue using a color scheme that employs navy blue and kelly green (other shades of green could be fine too) as well as our "E" logo.

Industry/Entity Type

Law Firm

```html
<!DOCTYPE html>
<html lang="en">
<head>
<meta charset="utf-8">
<title>Dorian Halvorsk, P.A. — Business Card</title>
<link rel="stylesheet" href="https://fonts.googleapis.com/css2?family=Cinzel:wght@600;700&family=Tinos&display=swap">
<style>
  :root {
    --navy: #1f2e63;
    --navy-deep: #182655;
    --navy-glow: #4f5a8e;
    --green: #0e7a3c;
    --green-bright: #08924a;
    --cream: #fbfaf1;
    --rust: #a63a22;
    --white: #ffffff;
    --stage: #e6e4df;
  }
  * { margin: 0; padding: 0; box-sizing: border-box; }
  html, body { width: 1200px; height: 1200px; overflow: hidden; }
  body { background: var(--stage); position: relative; font-family: "Tinos", serif; }

  .card { position: absolute; left: 124px; width: 944px; height: 554px; overflow: hidden; box-shadow: 0 4px 14px rgba(0,0,0,.25); }
  .card-front { top: 30px; background: var(--cream); }
  .card-back { top: 614px; height: 552px; background: radial-gradient(ellipse 420px 380px at 210px 300px, var(--navy-glow), var(--navy) 75%); }

  .mark-square { position: absolute; background: var(--navy); border: 3px solid var(--white); outline: 2px solid var(--navy); }
  .card-front .mark-square { left: 38px; top: 43px; width: 222px; height: 222px; }

  .firm-name { font-family: "Cinzel", serif; font-weight: 700; color: var(--navy); white-space: nowrap; }
  .firm-tagline { font-family: "Cinzel", serif; font-weight: 600; color: var(--rust); white-space: nowrap; }
  .card-front .firm-name { position: absolute; left: 286px; top: 80px; font-size: 45px; letter-spacing: 1px; }
  .card-front .firm-tagline { position: absolute; left: 287px; top: 142px; font-size: 33px; letter-spacing: 1px; }

  .rule { position: absolute; left: 0; top: 274px; width: 100%; height: 4px; background: var(--navy); }
  .rule-accent { position: absolute; left: 473px; top: 280px; right: 0; height: 3px; background: var(--green); }

  .panel-person { position: absolute; left: 0; top: 286px; width: 473px; height: 224px; background: var(--navy);
    color: var(--white); text-align: center; padding-top: 60px; }
  .person-name { font-size: 39px; line-height: 44px; }
  .person-title { font-size: 33px; line-height: 42px; }

  .panel-contact { position: absolute; left: 473px; top: 286px; right: 0; height: 224px;
    background: linear-gradient(90deg, var(--green) 0%, #10703a 100%); color: var(--white); padding: 22px 0 0 37px; font-size: 24px; }
  .panel-contact p { line-height: 37px; white-space: nowrap; }
  .panel-contact .gap { margin-top: 10px; }

  .web-strip { position: absolute; left: 0; top: 510px; width: 100%; height: 44px;
    background: linear-gradient(90deg, var(--green) 0 272px, var(--navy) 272px); color: var(--white);
    text-align: center; font-size: 23px; line-height: 44px; letter-spacing: 1px; font-weight: 700; }

  .back-shape { position: absolute; inset: 0; }
  .card-back .mark-square { left: 370px; top: 136px; width: 204px; height: 204px; box-shadow: 0 0 24px rgba(0,0,0,.45); }
  .card-back .firm-name { position: absolute; left: 0; right: 0; top: 355px; text-align: center; color: var(--white); font-size: 48px; letter-spacing: 1px; }
  .card-back .firm-tagline { position: absolute; left: 0; right: 0; top: 424px; text-align: center; color: var(--white); font-size: 30px; letter-spacing: 1px; }
</style>
</head>
<body>

<section class="card card-front">
  <div class="mark-square"></div>
  <h1 class="firm-name">DORIAN HALVORSK, P.A.</h1>
  <p class="firm-tagline">PERSONAL INJURY ATTORNEYS</p>
  <div class="rule"></div>
  <div class="rule-accent"></div>
  <div class="panel-person">
    <p class="person-name">Dorian Halvorsk</p>
    <p class="person-title">Attorney at Law</p>
  </div>
  <div class="panel-contact">
    <p>2150 Harborview Parkway Suite 410</p>
    <p>Palm Grove, Florida 34219</p>
    <p class="gap">Phone: 941.555.0182</p>
    <p>Fax: 941.555.0247</p>
    <p>Email: dorian@halvorsklaw.com</p>
  </div>
  <div class="web-strip">WWW.HALVORSKLAW.COM</div>
</section>

<section class="card card-back">
  <svg class="back-shape" width="944" height="552" viewBox="0 0 944 552" aria-hidden="true">
    <path d="M944 0 H470 C330 60 300 260 380 552 H944 Z" fill="var(--green-bright)"/>
  </svg>
  <div class="mark-square"></div>
  <h2 class="firm-name">DORIAN HALVORSK, P.A.</h2>
  <p class="firm-tagline">PERSONAL INJURY ATTORNEYS</p>
</section>

</body>
</html>
```